Vela Stewardship Business Card design

We need a creative business card design for our hospitality management company
We need the following information:
Our business Logo: Vela Stewardship
Name: Mara Dobrinsky
Phone number: 0458 317 642
Email: mara@velastewardship.com.au
Address: 214/53 Penrose Street, South Melbourne 3206
Web: www.velastewardship.com.au
I need the design to be a working file so that I can insert the names and numbers of the other staff members of our business.
The cards need to be 90 x 40mm
Thanks
Industry/Entity Type
Hospitality
Look and feel

```html
<!DOCTYPE html>
<html lang="en">
<head>
<meta charset="utf-8">
<title>Vela Stewardship – Business Card</title>
<link rel="stylesheet" href="https://fonts.googleapis.com/css2?family=Roboto+Condensed:wght@400;700&family=Questrial&display=swap">
<style>
  :root {
    --page-bg: #e9ebee;
    --navy-deep: #0c2344;
    --navy-mid: #1b3d66;
    --navy-glow: #6f8fb4;
    --ink-white: #ffffff;
    --ink-soft: #dfe7f1;
    --band-white: #f4f6f9;
    --band-blue-top: #9fb6d3;
    --band-blue-bottom: #5d7fa9;
  }
  * { box-sizing: border-box; margin: 0; padding: 0; }
  html, body {
    width: 1200px;
    height: 646px;
    overflow: hidden;
    background: var(--page-bg);
  }
  .canvas {
    position: relative;
    width: 1200px;
    height: 646px;
  }
  .business-card {
    position: absolute;
    left: 100px;
    top: 63px;
    width: 1000px;
    height: 520px;
    overflow: hidden;
    color: var(--ink-white);
    background:
      radial-gradient(ellipse 520px 300px at 42% 6%, var(--navy-glow) 0%, rgba(111,143,180,0.35) 40%, rgba(27,61,102,0) 75%),
      linear-gradient(160deg, var(--navy-mid) 0%, var(--navy-deep) 70%);
    box-shadow: 0 6px 18px rgba(12,35,68,0.25);
  }
  .holder {
    position: absolute;
    right: 60px;
    top: 38px;
    text-align: right;
  }
  .holder-name {
    font-family: "Roboto Condensed", sans-serif;
    font-weight: 700;
    font-size: 42px;
    line-height: 1.05;
  }
  .holder-role {
    font-family: "Roboto Condensed", sans-serif;
    font-weight: 400;
    font-size: 22px;
    color: var(--ink-soft);
  }
  .contact-list {
    position: absolute;
    right: 60px;
    top: 170px;
    list-style: none;
    text-align: right;
    font-family: "Questrial", sans-serif;
    font-size: 22px;
    line-height: 1.5;
    color: var(--ink-soft);
  }
  .contact-label {
    display: inline-block;
    width: 26px;
    margin-left: 10px;
    text-align: left;
    color: var(--ink-white);
  }
  .company-mark {
    position: absolute;
    left: 60px;
    top: 190px;
    display: flex;
    align-items: center;
    gap: 14px;
  }
  .company-square {
    width: 46px;
    height: 46px;
    background: var(--ink-white);
  }
  .company-name {
    font-family: "Roboto Condensed", sans-serif;
    font-weight: 700;
    font-size: 30px;
    letter-spacing: 0.5px;
    text-transform: uppercase;
  }
  .address {
    position: absolute;
    left: 60px;
    top: 318px;
    font-family: "Questrial", sans-serif;
    font-style: normal;
    font-size: 25px;
    line-height: 1.4;
    color: var(--ink-soft);
  }
  .band-white {
    position: absolute;
    left: 0;
    right: 0;
    top: 466px;
    height: 12px;
    background: var(--band-white);
  }
  .band-blue {
    position: absolute;
    left: 0;
    right: 0;
    top: 478px;
    bottom: 0;
    background: linear-gradient(180deg, var(--band-blue-top), var(--band-blue-bottom));
  }
</style>
</head>
<body>
  <main class="canvas">
    <section class="business-card" aria-label="Vela Stewardship business card">
      <header class="holder">
        <h1 class="holder-name">Mara Dobrinsky</h1>
        <p class="holder-role">Managing Director</p>
      </header>

      <ul class="contact-list">
        <li>0458 317 642<span class="contact-label">T:</span></li>
        <li>mara@velastewardship.com.au<span class="contact-label">E:</span></li>
        <li>www.velastewardship.com.au<span class="contact-label">W:</span></li>
      </ul>

      <div class="company-mark">
        <span class="company-square"></span>
        <span class="company-name">Vela Stewardship</span>
      </div>

      <address class="address">
        Vela Stewardship<br>
        214/53 Penrose Street,<br>
        South Melbourne 3206
      </address>

      <div class="band-white"></div>
      <div class="band-blue"></div>
    </section>
  </main>
</body>
</html>
```